New Packaging and label for New Beard Oil and Shampoo brand from London

Oils, Shampoo ect .. Beard Oil Ingredients: Application Directions: Apply to beard by weight in a small amount of oil will naturally absorb. Leaving it soft & conditioned. Ingredients: Coconut oil, scented oil, Oud oil, vitamin E 100% Natural `i will have 5 types of oils Vanilla Oud Rose Oud Cocktail Tea tree Velvet Dusk

Target Market(s)

A fashionable well groomed professional gentleman who is willing to invest in his appearance.

Industry/Entity Type

It Company

Font styles to use
Sans Serif

Colors

Designer to choose colors to be used in the design.

Requirements
Must have
• Beard Oil Ingredients: Application Directions: Apply to a beard by a small amount of oil will naturally absorb. Leaving it soft & conditioned. Ingredients: Coconut Oil, Scented Oil, Oil Oud, Vitamin E 100% Natural 1.0z 30ml Made in Uk i will have 5 types of oils Vanilla Oud Rose Oud Cocktail Tea Tree Velvet Beard Dusk Shampoo APPLICATION DIRECTIONS Massage into the beard / hair and rinse out with warm water. Distorted shampoos, there are no nasty chemicals which are damaging your beard instead of the wheat proteins and oils that you add to the hair follicles with nutrients and naturally adding a protective coating. INGREDIENTS Aqua (Water), Capryl / caprylyl glucoside, Cocomidopropyl betaine, Glycerin (Veg), Xanthan gum, Phenoxyethanol, Hydrolysed wheat protein, Aloe barbadensis (Aloe vera) leaf powder, Sodium benzoate, Potassium sorbate1 3.4 oz, 100ml Cylinder packaging for the Oils, Box for the shampoo
Nice to have
• I want "London" written underneath the logo and oil name.

```html
<!DOCTYPE html>
<html lang="en">
<head>
<meta charset="utf-8">
<title>Vanilla Oud Beard Oil Label</title>
<link rel="stylesheet" href="https://fonts.googleapis.com/css2?family=Questrial&display=swap">
<style>
  :root {
    --stage: #161616;
    --label-black: #000000;
    --panel-black: #0f0f0f;
    --gold: #b8964a;
    --white: #f4f4f4;
  }
  * { margin: 0; padding: 0; box-sizing: border-box; }
  html, body {
    width: 1200px;
    height: 886px;
    overflow: hidden;
    background: linear-gradient(180deg, #000 0%, #0c0c0c 45%, var(--stage) 100%);
    font-family: "Questrial", sans-serif;
  }
  .label {
    position: absolute;
    left: 50px;
    top: 203px;
    width: 1100px;
    height: 480px;
    background: var(--label-black);
  }
  .back-panel {
    position: absolute;
    left: 57px;
    top: 104px;
    width: 300px;
  }
  .section-title {
    color: var(--gold);
    font-size: 18px;
    line-height: 24px;
  }
  .section-body {
    color: var(--white);
    font-size: 18.5px;
    line-height: 23px;
    padding-left: 10px;
  }
  .section-body + .section-title { margin-top: 24px; }
  .origin {
    color: var(--gold);
    font-size: 18px;
    margin-top: 26px;
    padding-left: 47px;
  }
  .front-panel {
    position: absolute;
    left: 383px;
    top: 0;
    width: 337px;
    height: 480px;
    background: linear-gradient(90deg, #0a0a0a 0%, var(--panel-black) 50%, #0a0a0a 100%);
    text-align: center;
  }
  .brand-name {
    position: absolute;
    left: 0;
    right: 0;
    top: 112px;
    color: var(--white);
    font-size: 34px;
    line-height: 40px;
    letter-spacing: 1px;
  }
  .product-name {
    position: absolute;
    left: 0;
    right: 0;
    top: 290px;
    color: var(--white);
    font-size: 39px;
    line-height: 46px;
  }
  .product-city {
    position: absolute;
    left: 0;
    right: 0;
    top: 344px;
    color: var(--gold);
    font-size: 24px;
    line-height: 28px;
  }
  .volume {
    position: absolute;
    left: 0;
    right: 0;
    top: 432px;
    color: var(--white);
    font-size: 24px;
    line-height: 28px;
  }
  .volume small { font-size: 17px; }
</style>
</head>
<body>
  <div class="label">
    <div class="back-panel">
      <p class="section-title">Application Directions:</p>
      <p class="section-body">Apply to beard by rubbing<br>in a small amount the oil will<br>naturally absorb. Leaving it<br>soft &amp; conditioned.</p>
      <p class="section-title">Ingredients:</p>
      <p class="section-body">Coconut oil, scented oil,<br>Oud oil, vitamin E %100<br>Natural</p>
      <p class="origin">Made in Uk</p>
    </div>
    <div class="front-panel">
      <p class="brand-name">KINGSWAY<br>GROOMING</p>
      <p class="product-name">Vanilla Oud</p>
      <p class="product-city">London</p>
      <p class="volume">1 oz <small>(30 ml)</small></p>
    </div>
  </div>
</body>
</html>
```